A postcard needed for a kids gym

We are a kids gym opening soon. We are called Bouncewell Kids Gym. Here is the website so that you can get more details on what it is we will be doing. www.Bouncewellkidsgym.example I am including a screen shot of wallpaper we are using on two walls that will be prominently displayed in our building. I was wondering if the wall paper can somehow be included in the postcard as a soft background or something?no postage or mail info needed as this will be passed out by hand. I am also sending our logo and colors. Thank you for your help, and we look forward to hearing and seeing what you have to present. Sincerely,Lorraine

Target Market(s)

Parents

Industry/Entity Type

Childcare

Requirements
Must have
• "Opening soon"

```html
<!DOCTYPE html>
<html lang="en">
<head>
<meta charset="utf-8">
<title>Bouncewell Kids Gym – Opening Soon Postcard</title>
<link href="https://fonts.googleapis.com/css2?family=Fredoka:wght@600&family=Raleway:wght@400;500;700;800&family=Josefin+Slab:wght@400;600&display=swap" rel="stylesheet">
<style>
:root{
  --teal:#6cc3bf;
  --orange:#f7a940;
  --green:#8cc63f;
  --blue:#29a8e0;
  --yellow:#f9c80e;
  --white:#ffffff;
  --ink:#4a4a4a;
  --rule:#b9b9b9;
  --page:#eeeeec;
}
*{box-sizing:border-box;margin:0;padding:0}
html,body{width:895px;height:1200px;overflow:hidden;background:var(--page)}
body{position:relative;font-family:"Raleway",sans-serif}
.card{position:absolute;width:694px;height:537px;background:var(--white);overflow:hidden;box-shadow:0 2px 8px rgba(0,0,0,.18)}
.card--front{left:62px;top:43px}
.card--back{left:140px;top:615px}
.abs{position:absolute}

/* shared */
.brand{position:absolute;text-align:center;font-family:"Raleway",sans-serif;font-weight:800;color:var(--blue);line-height:1}
.brand__name{display:block}
.brand__sub{display:block;color:var(--green);letter-spacing:2px}
.banner-title{font-family:"Fredoka",sans-serif;font-weight:600;color:var(--white);letter-spacing:1px;line-height:1;white-space:nowrap}
.tab{position:absolute;border-radius:50%;display:flex;align-items:center;justify-content:center;color:var(--white);font-family:"Raleway",sans-serif;font-weight:500;box-shadow:2px 2px 4px rgba(0,0,0,.15)}
.tab--play{background:var(--blue)}
.tab--parties{background:var(--orange)}
.tab--classes{background:var(--yellow)}
.photo{position:absolute}

/* front */
.front__opening{left:32px;top:30px;color:var(--white);font-weight:400;font-size:29px;line-height:1.2}
.front__tagline{left:32px;top:118px;color:var(--white);font-size:15px;line-height:1.35}
.front__brand{left:300px;top:48px;width:380px}
.front__brand .brand__name{font-size:50px}
.front__brand .brand__sub{font-size:20px;margin-top:8px}
.front__banner{left:0;top:192px;width:694px;text-align:center;font-size:50px}
.front__panel{left:0;top:250px;width:345px;height:286px;background:var(--green)}
.front__heading{left:30px;top:265px;color:var(--white);font-size:19px;font-weight:500}
.front__copy{left:26px;top:296px;width:258px;color:var(--white);font-size:14px;line-height:1.4;text-align:justify}
.front__url{left:0;top:482px;width:339px;height:38px;background:var(--white);color:var(--ink);font-size:17px;padding:8px 0 0 34px}
.front .tab{width:84px;height:84px;font-size:17px}

/* back */
.back__brand{left:22px;top:28px;width:300px}
.back__brand .brand__name{font-size:40px}
.back__brand .brand__sub{font-size:16px;margin-top:6px}
.back__band{left:0;top:115px;width:370px;height:45px;background:var(--orange)}
.back__banner{left:42px;top:123px;font-size:30px}
.back__copy{left:20px;top:290px;width:330px;color:var(--white);font-family:"Josefin Slab",serif;font-size:12.5px;line-height:1.25}
.back .tab{width:80px;height:80px;font-size:16px}
.back__address{left:373px;top:26px;color:var(--ink);font-family:"Raleway",sans-serif;font-size:15px;line-height:1.3}
.back__address .name{color:var(--blue)}
.stamp{left:586px;top:29px;width:80px;height:56px;border:1.5px solid var(--rule)}
.mail-line{left:456px;width:210px;height:1.5px;background:var(--rule)}
</style>
</head>
<body>

<section class="card card--front front" aria-label="Postcard front">
  <svg class="abs" style="left:0;top:0" width="694" height="537" viewBox="0 0 694 537" aria-hidden="true">
    <path d="M0 0H282Q300 80 270 200L0 210Z" fill="var(--teal)"/>
    <path d="M0 200Q340 160 694 172V252H0Z" fill="var(--orange)"/>
  </svg>
  <div class="abs front__opening">OPENING<br>December 2015</div>
  <div class="abs front__tagline">Indoor play space &amp;<br>treatment center</div>
  <div class="brand front__brand"><span class="brand__name">Bouncewell</span><span class="brand__sub">KIDS GYM</span></div>
  <div class="abs banner-title front__banner">OPENING SOON</div>
  <div class="abs front__panel"></div>
  <div class="abs front__heading">Bouncewell Kids Gym</div>
  <p class="abs front__copy">provides fun for the entire family with an inclusive indoor play area, designated space for parties or celebrations, and a variety of motivating, kid-centered classes. We also offer private therapy services you can easily schedule by phone or online.</p>
  <div class="abs front__url">www.Bouncewellkidsgym.example</div>
  <div class="photo" role="img" aria-label="Photo of children playing among large colourful foam blocks" style="left:339px;top:251px;width:355px;height:286px;background:linear-gradient(135deg,#d23a2e 0%,#f2d21a 35%,#2b63c6 60%,#f0c21a 80%,#c83327 100%)"></div>
  <div class="tab tab--play" style="left:297px;top:251px">play</div>
  <div class="tab tab--parties" style="left:297px;top:324px">parties</div>
  <div class="tab tab--classes" style="left:297px;top:401px">classes</div>
</section>

<section class="card card--back back" aria-label="Postcard back">
  <div class="brand back__brand"><span class="brand__name">Bouncewell</span><span class="brand__sub">KIDS GYM</span></div>
  <div class="abs back__band"></div>
  <div class="abs banner-title back__banner">OPENING SOON</div>
  <div class="photo" role="img" aria-label="Photo of the gym interior with wooden climbing structures and slide" style="left:0;top:160px;width:380px;height:125px;background:linear-gradient(90deg,#8a7a66,#d8c8a8 40%,#5e6f44 75%,#cfc2a6)"></div>
  <svg class="abs" style="left:0;top:0" width="694" height="537" viewBox="0 0 694 537" aria-hidden="true">
    <path d="M0 285H395Q405 360 380 440H0Z" fill="var(--green)"/>
    <path d="M290 0Q430 240 345 537" fill="none" stroke="var(--green)" stroke-width="8"/>
  </svg>
  <p class="abs back__copy">Bouncewell Kids Gym (BKGym) is more than an activity center. Our facility offers a safe, inclusive space for kids to play, learn, and explore using all their senses. With specialized equipment to encourage development and boost confidence, families can provide their children sensory and motor experiences rooted in fun, surrounded by peers. One-on-one private therapy services are also available by appointment.</p>
  <div class="photo" role="img" aria-label="Photo of a children's birthday party with balloons" style="left:0;top:440px;width:190px;height:97px;background:linear-gradient(135deg,#e87a9a,#f4b048 50%,#5aa5d8)"></div>
  <div class="photo" role="img" aria-label="Photo of young children playing in a class" style="left:192px;top:440px;width:180px;height:97px;background:linear-gradient(135deg,#7fc3e8,#f2e2c8 50%,#e8a25a)"></div>
  <div class="tab tab--play" style="left:359px;top:154px">play</div>
  <div class="tab tab--parties" style="left:359px;top:228px">parties</div>
  <div class="tab tab--classes" style="left:359px;top:304px">classes</div>
  <div class="abs back__address"><span class="name">Bouncewell Kids Gym</span><br>482 Maple Grove Lane<br>Fairview, CA 90000<br>bouncewellkidsgym.example</div>
  <div class="abs stamp"></div>
  <div class="abs mail-line" style="top:229px"></div>
  <div class="abs mail-line" style="top:269px"></div>
  <div class="abs mail-line" style="top:310px"></div>
  <div class="abs mail-line" style="top:351px"></div>
</section>

</body>
</html>
```